New PowerPoint Design Project

A well-known speaker needs a visual presence that compliments his amazing, consistent performance onstage. You'll easily improve this deck, and I'll leave it to you whether you stick with the palette defined by the original PLMVUE icons you'll find in the deck, the mishmosh in the deck as it stands, OR get extra points by going with the corporate color palette so our speaking slides fit with Marlon's brands and his three sub-brands. A look at the Marlon subbrand .png in the attached zip file might give you some ideas.
Updates

Just noting that I'm available to answer questions or supply assets you think you'd need. The big design issue I'm looking for someone to solve is how you'll treat the bright clusters of icons in information graphics of the deck.

Target Market(s)

Corporate Executives and wanabees

Requirements
Must have
• The footer needs to have the Dunwoody Sparkpath logo and Twitter and Facebook link and you need to do the first 27 slides. The slides past 27 are there simply if you want to use assets from those slides.
Nice to have
• Use the palette document in the zip rather than palette dictated by the PLMVUE icons in the deck (I do not have source for the icons.).

```html
<!DOCTYPE html>
<html lang="en">
<head>
<meta charset="utf-8">
<title>Dunwoody Sparkpath – Presentation Design</title>
<link rel="stylesheet" href="https://fonts.googleapis.com/css2?family=Arimo:wght@400;700&family=Mulish:wght@400;600&display=swap">
<style>
:root{
  --navy:#34598f;
  --navy-dark:#2d4a7c;
  --footer:#3b5d93;
  --teal:#176e6c;
  --green:#5a7e3a;
  --lime:#b5c53e;
  --yellow:#f2bd3c;
  --ink:#1d1d1d;
  --grey:#7a7a7a;
  --axis:#9a9a9a;
  --white:#ffffff;
  --cover-blue:#2f8fd0;
  --cover-orange:#ef6b24;
}
*{margin:0;padding:0;box-sizing:border-box}
html,body{width:1200px;height:1000px;overflow:hidden;background:var(--white)}
body{position:relative;font-family:"Arimo",Arial,sans-serif;color:var(--ink)}
h2{font-weight:400}
.page-title{position:absolute;top:30px;left:0;width:1200px;text-align:center;font-family:"Mulish",sans-serif;font-weight:400;font-size:29px;color:var(--navy-dark)}
.slide{position:absolute;width:376px;height:282px;background:var(--white);overflow:hidden}
.slide--cover{background:var(--navy)}
.col-1{left:22px}.col-2{left:416px}.col-3{left:808px}
.row-1{top:105px}.row-2{top:400px}.row-3{top:695px}
.footer{position:absolute;left:0;bottom:0;width:100%;height:20px;background:var(--footer);display:flex;align-items:center;padding:0 10px;color:var(--white);font-size:8px}
.slide--cover .footer{background:transparent}
.brand{display:flex;align-items:center;gap:5px;font-family:"Mulish",sans-serif;font-weight:400;font-size:10px;color:#c9d4e6;letter-spacing:.2px;white-space:nowrap}
.brand-mark{width:9px;height:9px;background:#c9d4e6;flex:none}
.social{margin-left:auto;display:flex;gap:12px}
.social-item{display:flex;align-items:center;gap:3px;font-size:7.5px}
.social-box{width:9px;height:9px;background:var(--white)}
.cover-brand{position:absolute;top:27px;left:190px;font-size:14.5px;color:#dfe6f1;gap:7px;letter-spacing:0}
.cover-brand .brand-mark{width:14px;height:14px;background:#dfe6f1}
.cover-title{position:absolute;top:89px;left:138px;font-size:12.5px;color:var(--white);letter-spacing:.2px}
.cover-date{position:absolute;top:112px;left:298px;font-size:7.5px;color:#8fa8cc}
.cover-title--end{left:280px;top:87px}
.cover-date--end{left:295px;top:110px}
.statement{position:absolute;left:53px;top:54px;font-weight:700;letter-spacing:3px;color:var(--navy-dark)}
.statement .light{font-weight:400}
.statement-line1{font-size:24px}
.statement-line2,.statement-line3{font-size:17px;color:var(--grey);font-weight:400;letter-spacing:2.5px;margin-top:14px}
.statement-line3{margin-top:2px}
.statement-line2 b,.statement-line3 b{font-weight:700}
.statement-line4{font-size:33px;margin-top:12px;letter-spacing:1.5px}
.science-title{position:absolute;left:22px;top:26px;font-size:14px;line-height:16px;letter-spacing:.3px}
.science-list{position:absolute;left:22px;top:71px;width:160px;list-style:none;font-size:8.5px;line-height:10px;color:#444}
.science-list li{margin-bottom:11px;padding-left:10px;position:relative}
.science-list li::before{content:"•";position:absolute;left:0}
.book{position:absolute;top:92px;height:100px}
.book--blue{left:215px;width:63px;background:var(--cover-blue)}
.book--orange{left:282px;width:47px;background:var(--cover-orange)}
.trust-word{position:absolute;left:40px;top:35px;font-size:34px;color:var(--navy)}
.trust-sub{position:absolute;left:190px;top:44px;font-size:12px;line-height:14px;color:var(--navy);text-align:center}
.tile{position:absolute;display:flex;align-items:center;justify-content:center;color:var(--white);font-size:10px}
.tile--personal{left:38px;top:80px;width:143px;height:50px;background:var(--teal)}
.tile--professional{left:187px;top:80px;width:142px;height:50px;background:var(--green)}
.tile--structural{left:38px;top:137px;width:291px;height:50px;background:var(--navy)}
.step-title{position:absolute;left:23px;top:27px;font-size:13px}
.step-sub{position:absolute;left:23px;top:44px;font-size:9px}
.missions{position:absolute;left:33px;top:81px}
.trends-title{position:absolute;left:72px;top:20px;font-size:18px;color:var(--navy)}
.trends-title small{font-size:12px}
.trends-favor{position:absolute;left:144px;top:44px;font-size:18px;font-weight:700;color:var(--green)}
.trends-diagram{position:absolute;left:0;top:0}
.trends-note{position:absolute;left:0;top:236px;width:100%;text-align:center;font-size:7.5px;line-height:10px;color:#555}
.trends-note b{color:var(--navy)}
.chart-title{position:absolute;left:25px;top:38px;font-size:14px}
.chart{position:absolute;left:0;top:0}
.chart text{font-family:"Arimo",Arial,sans-serif}
</style>
</head>
<body>
<h1 class="page-title">Sample Design</h1>

<section class="slide slide--cover col-1 row-1">
  <div class="brand cover-brand"><span class="brand-mark"></span>dunwoodysparkpath</div>
  <div class="cover-title">PRESENTATION DESIGN TEMPLATE</div>
  <div class="cover-date">October 23, 2013</div>
  <footer class="footer">
    <div class="social"><span class="social-item"><span class="social-box"></span>/MarlonDunwoody</span><span class="social-item"><span class="social-box"></span>@dunwoody</span></div>
  </footer>
</section>

<section class="slide col-2 row-1">
  <div class="statement">
    <div class="statement-line1">NOT <span class="light">A</span> SPEECH</div>
    <div class="statement-line2">START <b>OF</b> A <b>DIALOG</b></div>
    <div class="statement-line3"><b>MOVING</b> TO</div>
    <div class="statement-line4">ACTION</div>
  </div>
  <footer class="footer">
    <div class="brand"><span class="brand-mark"></span>dunwoodysparkpath</div>
    <div class="social"><span class="social-item"><span class="social-box"></span>/MarlonDunwoody</span><span class="social-item"><span class="social-box"></span>@dunwoody</span></div>
  </footer>
</section>

<section class="slide col-3 row-1">
  <h2 class="science-title">WE HAVE MADE BEHAVIORAL<br>TRANSFORMATION A SCIENCE</h2>
  <ul class="science-list">
    <li>20 years of study</li>
    <li>Relational and Collaborative Focus</li>
    <li>Constantly refining the methodologies</li>
    <li>Field testing, consulting and training with 100s of Apex 1000 clients</li>
  </ul>
  <div class="book book--blue" role="img" aria-label="Book cover, blue"></div>
  <div class="book book--orange" role="img" aria-label="Book cover, orange"></div>
  <footer class="footer">
    <div class="brand"><span class="brand-mark"></span>dunwoodysparkpath</div>
    <div class="social"><span class="social-item"><span class="social-box"></span>/MarlonDunwoody</span><span class="social-item"><span class="social-box"></span>@dunwoody</span></div>
  </footer>
</section>

<section class="slide col-1 row-2">
  <div class="trust-word">TRUST :</div>
  <div class="trust-sub">3 DIMENSIONS<br>TO CONSIDER</div>
  <div class="tile tile--personal">PERSONAL</div>
  <div class="tile tile--professional">PROFESSIONAL</div>
  <div class="tile tile--structural">STRUCTURAL</div>
  <footer class="footer">
    <div class="brand"><span class="brand-mark"></span>dunwoodysparkpath</div>
    <div class="social"><span class="social-item"><span class="social-box"></span>/MarlonDunwoody</span><span class="social-item"><span class="social-box"></span>@dunwoody</span></div>
  </footer>
</section>

<section class="slide col-2 row-2">
  <div class="step-title">STEP <b>ONE</b></div>
  <div class="step-sub">PREPARATION</div>
  <svg class="missions" width="323" height="156" viewBox="0 0 323 156" font-family="Arimo, Arial, sans-serif" font-size="8.5" fill="#fff">
    <g>
      <rect x="0" y="0" width="323" height="34" fill="var(--navy)"/>
      <polyline points="78,0 92,17 78,34" fill="none" stroke="#fff" stroke-width="1"/>
      <text x="18" y="20">MISSION 01</text><text x="117" y="20">ESTABLISH LARGER GOAL</text>
    </g>
    <g transform="translate(0,40)">
      <rect width="323" height="34" fill="var(--teal)"/>
      <polyline points="78,0 92,17 78,34" fill="none" stroke="#fff"/>
      <text x="18" y="20">MISSION 02</text><text x="117" y="15">ASK RIGHT QUESTIONS</text><text x="117" y="26">AND PROVIDE SEMI - STRUCTURE</text>
    </g>
    <g transform="translate(0,80)">
      <rect width="323" height="34" fill="var(--green)"/>
      <polyline points="78,0 92,17 78,34" fill="none" stroke="#fff"/>
      <text x="18" y="20">MISSION 03</text><text x="117" y="20">FOCUS ON ISSUES BY PROVIDING DATA</text>
    </g>
    <g transform="translate(0,120)">
      <rect width="323" height="34" fill="var(--lime)"/>
      <polyline points="78,0 92,17 78,34" fill="none" stroke="#fff"/>
      <text x="18" y="20">MISSION 04</text><text x="117" y="20">PRE – MEETING REFLECTIO</text>
    </g>
  </svg>
  <footer class="footer">
    <div class="brand"><span class="brand-mark"></span>dunwoodysparkpath</div>
    <div class="social"><span class="social-item"><span class="social-box"></span>/MarlonDunwoody</span><span class="social-item"><span class="social-box"></span>@dunwoody</span></div>
  </footer>
</section>

<section class="slide col-3 row-2">
  <div class="trends-title">TRENDS <small>ARE CONSPIRING IN</small></div>
  <div class="trends-favor">OUR FAVOR</div>
  <svg class="trends-diagram" width="376" height="282" viewBox="0 0 376 282" font-family="Arimo, Arial, sans-serif" font-size="5" fill="#fff" text-anchor="middle">
    <circle cx="140" cy="112" r="37" fill="var(--yellow)"/>
    <circle cx="237" cy="112" r="37" fill="var(--green)"/>
    <circle cx="140" cy="186" r="37" fill="var(--teal)"/>
    <circle cx="237" cy="186" r="37" fill="var(--lime)"/>
    <circle cx="188" cy="149" r="31" fill="var(--navy)" stroke="#fff" stroke-width="2"/>
    <text x="130" y="108">TALENT IS</text><text x="130" y="115">TAPPED OUT</text>
    <text x="245" y="104">COMPLEXITY</text><text x="245" y="111">CALLS FOR</text><text x="245" y="118">COLLABORATION</text>
    <text x="188" y="148">RELATIONAL</text><text x="188" y="155">COLLABORATION</text>
    <text x="133" y="190">TECH SUPERCHARGES</text><text x="133" y="197">COLLABORATIVE ACCESS</text>
    <text x="247" y="190">RELATIONAL SCIENCE</text><text x="247" y="197">HAS CAUGHT UP</text>
  </svg>
  <p class="trends-note">IGNORING “<b>RELATIONAL</b>” WILL MEAN <b>TROUBLE…</b><br>AND <b>TECHNOLOGY</b> LIKELY GETS <b>BLAMED</b></p>
  <footer class="footer">
    <div class="brand"><span class="brand-mark"></span>dunwoodysparkpath</div>
    <div class="social"><span class="social-item"><span class="social-box"></span>/MarlonDunwoody</span><span class="social-item"><span class="social-box"></span>@dunwoody</span></div>
  </footer>
</section>

<section class="slide col-1 row-3">
  <h2 class="chart-title">Sample Bar Chart</h2>
  <svg class="chart" width="376" height="282" viewBox="0 0 376 282" font-size="6" fill="#333">
    <line x1="75" y1="85" x2="75" y2="207" stroke="var(--axis)" stroke-width=".6"/>
    <line x1="75" y1="207" x2="305" y2="207" stroke="var(--axis)" stroke-width=".6"/>
    <g text-anchor="end">
      <text x="70" y="209">0</text><text x="70" y="192">1</text><text x="70" y="174">2</text><text x="70" y="157">3</text>
      <text x="70" y="139">4</text><text x="70" y="122">5</text><text x="70" y="105">6</text><text x="70" y="87">7</text>
    </g>
    <g>
      <rect x="94" y="132.2" width="7" height="74.8" fill="var(--navy)"/>
      <rect x="102" y="165.2" width="7" height="41.8" fill="var(--teal)"/>
      <rect x="110" y="172.2" width="7" height="34.8" fill="var(--green)"/>
      <rect x="118" y="120" width="7" height="87" fill="var(--lime)"/>
      <rect x="149" y="163.5" width="7" height="43.5" fill="var(--navy)"/>
      <rect x="157" y="130.4" width="7" height="76.6" fill="var(--teal)"/>
      <rect x="165" y="154.8" width="7" height="52.2" fill="var(--green)"/>
      <rect x="173" y="140.9" width="7" height="66.1" fill="var(--lime)"/>
      <rect x="204" y="146.1" width="7" height="60.9" fill="var(--navy)"/>
      <rect x="212" y="175.7" width="7" height="31.3" fill="var(--teal)"/>
      <rect x="220" y="102.6" width="7" height="104.4" fill="var(--green)"/>
      <rect x="228" y="158.3" width="7" height="48.7" fill="var(--lime)"/>
      <rect x="259" y="128.7" width="7" height="78.3" fill="var(--navy)"/>
      <rect x="267" y="158.3" width="7" height="48.7" fill="var(--teal)"/>
      <rect x="275" y="120" width="7" height="87" fill="var(--green)"/>
      <rect x="283" y="151.3" width="7" height="55.7" fill="var(--lime)"/>
    </g>
    <g text-anchor="middle" font-size="5.5">
      <text x="97.5" y="129">4.3</text><text x="105.5" y="162">2.4</text><text x="113.5" y="169">2</text><text x="121.5" y="117">5</text>
      <text x="152.5" y="160">2.5</text><text x="160.5" y="127">4.4</text><text x="168.5" y="152">3</text><text x="176.5" y="138">3.8</text>
      <text x="207.5" y="143">3.5</text><text x="215.5" y="173">1.8</text><text x="223.5" y="100">6</text><text x="231.5" y="155">2.8</text>
      <text x="262.5" y="126">4.5</text><text x="270.5" y="155">2.8</text><text x="278.5" y="117">5</text><text x="286.5" y="148">3.2</text>
      <text x="110" y="218">A</text><text x="165" y="218">B</text><text x="220" y="218">C</text><text x="275" y="218">D</text>
    </g>
    <g font-size="5.5">
      <circle cx="320" cy="132" r="1.3" fill="var(--navy)"/><text x="324" y="134">S1</text>
      <circle cx="320" cy="141" r="1.3" fill="var(--teal)"/><text x="324" y="143">S2</text>
      <circle cx="320" cy="150" r="1.3" fill="var(--green)"/><text x="324" y="152">S3</text>
      <circle cx="320" cy="159" r="1.3" fill="var(--lime)"/><text x="324" y="161">S4</text>
    </g>
  </svg>
  <footer class="footer">
    <div class="brand"><span class="brand-mark"></span>dunwoodysparkpath</div>
    <div class="social"><span class="social-item"><span class="social-box"></span>/MarlonDunwoody</span><span class="social-item"><span class="social-box"></span>@dunwoody</span></div>
  </footer>
</section>

<section class="slide col-2 row-3">
  <h2 class="chart-title">Sample Line Chart</h2>
  <svg class="chart" width="376" height="282" viewBox="0 0 376 282" font-size="5.5" fill="#333">
    <line x1="55" y1="65" x2="55" y2="212" stroke="var(--axis)" stroke-width=".6"/>
    <line x1="55" y1="212" x2="265" y2="212" stroke="var(--axis)" stroke-width=".6"/>
    <g text-anchor="end">
      <text x="50" y="214">0</text><text x="50" y="199">0.5</text><text x="50" y="185">1</text><text x="50" y="170">1.5</text>
      <text x="50" y="155">2</text><text x="50" y="141">2.5</text><text x="50" y="126">3</text><text x="50" y="111">3.5</text>
      <text x="50" y="97">4</text><text x="50" y="82">4.5</text><text x="50" y="67">5</text>
    </g>
    <g fill="none" stroke-width="1.2">
      <polyline points="77,85.6 133,138.5 188,109.1 242,79.7" stroke="var(--green)"/>
      <polyline points="77,141.4 133,82.6 188,159.1 242,129.7" stroke="var(--lime)"/>
      <polyline points="77,182.6 133,176.7 188,135.6 242,167.9" stroke="var(--navy)"/>
      <polyline points="77,200.2 133,112 188,79.7 242,103.2" stroke="var(--teal)"/>
    </g>
    <g>
      <rect x="75" y="83.6" width="4" height="4" fill="var(--green)"/><rect x="131" y="136.5" width="4" height="4" fill="var(--green)"/>
      <rect x="186" y="107.1" width="4" height="4" fill="var(--green)"/><rect x="240" y="77.7" width="4" height="4" fill="var(--green)"/>
      <circle cx="77" cy="141.4" r="2" fill="var(--lime)"/><circle cx="133" cy="82.6" r="2" fill="var(--lime)"/>
      <circle cx="188" cy="159.1" r="2" fill="var(--lime)"/><circle cx="242" cy="129.7" r="2" fill="var(--lime)"/>
      <circle cx="77" cy="182.6" r="1.8" fill="var(--navy)"/><circle cx="133" cy="176.7" r="1.8" fill="var(--navy)"/>
      <circle cx="188" cy="135.6" r="1.8" fill="var(--navy)"/><circle cx="242" cy="167.9" r="1.8" fill="var(--navy)"/>
      <circle cx="77" cy="200.2" r="1.8" fill="var(--teal)"/><circle cx="133" cy="112" r="1.8" fill="var(--teal)"/>
      <circle cx="188" cy="79.7" r="1.8" fill="var(--teal)"/><circle cx="242" cy="103.2" r="1.8" fill="var(--teal)"/>
    </g>
    <g text-anchor="middle">
      <text x="80" y="79">4.3</text><text x="80" y="135">2.4</text><text x="80" y="176" fill="#c0392b">1</text>
      <text x="78" y="194" font-size="8" font-weight="700">0.4</text>
      <text x="134" y="73">4.4</text><text x="135" y="100" font-size="8" font-weight="700">3.4</text><text x="134" y="126">2.5</text><text x="134" y="167">1.2</text>
      <text x="189" y="69" font-size="8" font-weight="700">4.5</text><text x="189" y="100">3.5</text><text x="189" y="125">2.6</text><text x="189" y="173">1.8</text>
      <text x="243" y="70">4.5</text><text x="243" y="94" font-size="8" font-weight="700">3.7</text><text x="243" y="119">2.8</text><text x="243" y="158">1.5</text>
      <text x="77" y="224">Category 1</text><text x="133" y="224">Category 2</text><text x="188" y="224">Category 3</text><text x="242" y="224">Category 4</text>
    </g>
    <g>
      <line x1="281" y1="160" x2="291" y2="160" stroke="var(--green)"/><rect x="284.5" y="158.5" width="3" height="3" fill="var(--green)"/><text x="295" y="162">Series 1</text>
      <line x1="281" y1="168" x2="291" y2="168" stroke="var(--lime)"/><circle cx="286" cy="168" r="1.5" fill="var(--lime)"/><text x="295" y="170">Series 2</text>
      <line x1="281" y1="176" x2="291" y2="176" stroke="var(--navy)"/><circle cx="286" cy="176" r="1.5" fill="var(--navy)"/><text x="295" y="178">Series 3</text>
      <line x1="281" y1="184" x2="291" y2="184" stroke="var(--teal)"/><circle cx="286" cy="184" r="1.5" fill="var(--teal)"/><text x="295" y="186">Series 4</text>
    </g>
  </svg>
  <footer class="footer">
    <div class="brand"><span class="brand-mark"></span>dunwoodysparkpath</div>
    <div class="social"><span class="social-item"><span class="social-box"></span>/MarlonDunwoody</span><span class="social-item"><span class="social-box"></span>@dunwoody</span></div>
  </footer>
</section>

<section class="slide slide--cover col-3 row-3">
  <div class="brand cover-brand"><span class="brand-mark"></span>dunwoodysparkpath</div>
  <div class="cover-title cover-title--end">THANK YOU</div>
  <div class="cover-date cover-date--end">October 23, 2013</div>
  <footer class="footer">
    <div class="social"><span class="social-item"><span class="social-box"></span>/MarlonDunwoody</span><span class="social-item"><span class="social-box"></span>@dunwoody</span></div>
  </footer>
</section>
</body>
</html>
```